Restaurant service company needs a website!

I am looking for a skilled web designer/developer to create a professional, responsive, and easy-to-navigate website for my company, which specializes in servicing restaurant cooking equipment. The site should communicate trust, reliability, and technical expertise to our target audience, restaurant owners, managers, and commercial kitchen operators. I have included the company logos, if any other format for them is needed please let me know.

Target Market(s)

restaurant owners, managers, and commercial kitchen operators

Industry/Entity Type

Commercial Kitchen Equipment Service

Coding

Coded - Design and coding required

Number of Pages Required

1 page

Font styles to use
Serif
Sans Serif

Requirements
Must have
• Contact and service request forms, Click-to-call functionality for mobile, Clean, modern layout with strong visuals, Easy navigation, mobile-friendly
Nice to have
• Testimonials or Reviews, If possible a click-to-text functionality for mobile.
Should not have
• Any mention of Refrigeration or HVAC, "Free Quotes"

```html
<!DOCTYPE html>
<html lang="en">
<head>
<meta charset="utf-8">
<title>Northgate Restaurant Service – Commercial Kitchen Equipment Repair</title>
<link rel="stylesheet" href="https://fonts.googleapis.com/css2?family=Poppins:wght@400;500;600;700&family=Inter:wght@400;500;600;700&display=swap">
<style>
:root{
  --teal:#0f8b7e;
  --teal-soft:#e3f3f0;
  --orange:#f47a1c;
  --orange-soft:#fdeee2;
  --navy:#1b2533;
  --navy-2:#2c3746;
  --ink:#1d2330;
  --muted:#6b7280;
  --faint:#9aa0a8;
  --line:#e3e6ea;
  --bg-soft:#f5f6f8;
  --field:#f1f2f4;
  --white:#ffffff;
  --gold:#f5b50a;
}
*{box-sizing:border-box;margin:0;padding:0}
html,body{width:1200px;height:3606px;overflow:hidden}
body{font-family:"Inter",sans-serif;color:var(--ink);background:var(--white);font-size:12px}
h1,h2,h3,h4{font-family:"Poppins",sans-serif;color:var(--ink)}
a{text-decoration:none}
.wrap{width:966px;margin:0 auto;position:relative}
.btn{display:inline-flex;align-items:center;justify-content:center;gap:6px;border-radius:999px;font-weight:600;font-family:"Inter",sans-serif;color:var(--white)}
.section-head{text-align:center}
.section-head h2{font-size:30px;font-weight:700}
.section-head p{font-size:13px;color:var(--muted);line-height:1.5;margin:10px auto 0;width:440px}

/* navigation */
.nav{height:64px;display:flex;align-items:center;justify-content:space-between;padding:0 88px;background:var(--white)}
.brand{font-weight:700;font-size:18px;color:var(--teal);letter-spacing:.5px;display:flex;align-items:center;gap:8px}
.brand .mark{width:12px;height:12px;background:var(--teal);border-radius:2px}
.nav-links{display:flex;gap:22px;font-size:12px;color:var(--ink);margin-left:110px}
.nav-cta{display:flex;gap:14px}
.nav-cta .btn{height:26px;padding:0 18px;font-size:11px}
.bg-teal{background:var(--teal)}
.bg-orange{background:var(--orange)}

/* hero */
.hero{height:512px;position:relative;overflow:hidden}
.hero-photo{position:absolute;inset:0;background:radial-gradient(ellipse at 60% 35%,#b07a45 0%,#6a4526 35%,#2f1f14 75%,#1c120b 100%)}
.hero-shade{position:absolute;inset:0;background:linear-gradient(90deg,rgba(0,0,0,.45),rgba(0,0,0,.1))}
.hero-copy{position:absolute;left:81px;top:152px}
.hero-copy h1{color:var(--white);font-size:58px;font-weight:600;line-height:1.05;width:520px}
.hero-copy p{color:#eee;font-size:18px;margin-top:22px}
.hero-actions{display:flex;gap:16px;margin-top:30px}
.hero-actions .btn{height:50px;font-size:14px}
.btn-primary{background:var(--teal);width:196px}
.btn-ghost{border:2px solid var(--white);width:138px}
.dots{position:absolute;left:50%;transform:translateX(-50%);bottom:26px;display:flex;gap:7px}
.dots span{width:9px;height:9px;border-radius:50%;background:rgba(255,255,255,.5)}
.dots span:first-child{background:var(--white)}

/* services */
.services{height:599px;background:var(--bg-soft);padding-top:50px}
.tabs{display:flex;justify-content:center;gap:12px;margin-top:48px}
.tab{height:32px;padding:0 16px;border-radius:999px;font-size:11px;display:flex;align-items:center;gap:6px;color:var(--ink)}
.tab.active{background:var(--teal);color:var(--white)}
.service-grid{display:grid;grid-template-columns:repeat(3,309px);gap:19px;margin-top:16px}
.service{background:var(--white);border-radius:8px;overflow:hidden;box-shadow:0 2px 8px rgba(0,0,0,.08);height:242px}
.service-photo{height:123px;position:relative}
.tag{position:absolute;top:12px;right:12px;background:var(--teal);color:var(--white);font-size:11px;font-weight:600;padding:3px 9px;border-radius:999px}
.service-body{padding:14px 16px}
.service-body h3{font-family:"Inter",sans-serif;font-size:13px;font-weight:600}
.service-body p{font-size:10.5px;color:var(--muted);line-height:1.5;margin-top:8px;height:32px}
.service-body .btn{width:100%;height:26px;border-radius:4px;background:var(--teal);font-size:11px;font-weight:500;margin-top:10px}
.services-more{text-align:center;margin-top:32px}
.services-more .btn{height:38px;width:210px;background:var(--orange);font-size:12px}

/* about */
.about{height:425px;padding-top:52px}
.about .wrap{display:flex;justify-content:space-between}
.about-text{width:450px;padding-top:12px}
.about-text h2{font-size:28px;font-weight:700}
.about-text p{font-size:12px;color:var(--muted);line-height:1.6;margin-top:16px}
.features{display:grid;grid-template-columns:1fr 1fr;gap:16px 30px;margin-top:22px}
.feature{display:flex;gap:12px}
.f-icon{width:26px;height:26px;border-radius:6px;background:var(--teal-soft);flex:none;display:flex;align-items:center;justify-content:center}
.feature h4{font-family:"Inter",sans-serif;font-size:11px;font-weight:600}
.feature p{font-size:9.5px;margin-top:4px;line-height:1.45}
.about-visual{position:relative;width:469px;height:319px}
.tech-photo{position:absolute;inset:0;border-radius:8px;background:linear-gradient(135deg,#1f3a46 0%,#3c5a63 40%,#b98a55 75%,#e8c28f 100%)}
.badge-rating{position:absolute;right:-15px;top:-16px;width:102px;height:64px;background:var(--orange);color:var(--white);border-radius:6px;padding:10px 14px}
.badge-years{position:absolute;left:-13px;bottom:-17px;width:113px;height:65px;background:var(--teal);color:var(--white);border-radius:6px;padding:12px 14px}
.badge-rating b,.badge-years b{font-size:20px;font-family:"Poppins",sans-serif}
.badge-rating span,.badge-years span{display:block;font-size:8.5px;margin-top:2px}

/* service request */
.request{height:621px;background:var(--bg-soft);padding-top:50px}
.request-grid{display:flex;justify-content:space-between;margin-top:52px}
.card{background:var(--white);border-radius:8px;box-shadow:0 2px 10px rgba(0,0,0,.07)}
.req-form{width:467px;height:419px;padding:22px 20px}
.req-form h3,.hours h3{font-family:"Inter",sans-serif;font-size:14px;font-weight:600}
.fields{display:grid;grid-template-columns:1fr 1fr;gap:16px;margin-top:14px}
.field label{display:block;font-size:9px;color:var(--ink);margin-bottom:6px}
.input{height:30px;border:1px solid var(--line);border-radius:4px;font-size:9px;color:var(--faint);display:flex;align-items:center;justify-content:space-between;padding:0 10px}
.input.sel{background:var(--field);color:var(--ink)}
.input.val{color:var(--ink)}
.field.full{grid-column:1/3}
.textarea{height:70px;align-items:flex-start;padding-top:10px}
.count{text-align:right;font-size:8px;color:var(--faint);margin-top:4px}
.submit{width:100%;height:38px;border-radius:4px;background:var(--teal);color:var(--white);font-size:12px;font-weight:600;display:flex;align-items:center;justify-content:center;margin-top:12px}
.req-side{width:469px}
.assist{background:var(--teal);border-radius:8px;height:190px;padding:22px;color:var(--white);display:block}
.assist h3{color:var(--white);font-family:"Inter",sans-serif;font-size:14px;font-weight:600}
.assist-item{display:flex;gap:14px;align-items:center;margin-top:22px;color:var(--white)}
.assist-icon{width:30px;height:30px;border-radius:6px;background:rgba(255,255,255,.18);display:flex;align-items:center;justify-content:center}
.assist-item b{font-size:10px;display:block}
.assist-item span{font-size:9.5px;opacity:.85}
.hours{height:169px;margin-top:20px;padding:22px 20px}
.hours-list{margin-top:14px}
.hours-row{display:flex;justify-content:space-between;font-size:10px;padding:9px 0;border-bottom:1px solid #f0f1f3;color:var(--muted)}
.hours-row:last-child{border:0}
.hours-row b{color:var(--ink);font-weight:600}

/* reviews */
.reviews{height:538px;padding-top:40px}
.review-grid{display:grid;grid-template-columns:repeat(3,309px);gap:15px 19px;margin-top:36px}
.review{height:117px;padding:16px;border:1px solid var(--line);border-radius:6px;background:var(--white);box-shadow:0 1px 4px rgba(0,0,0,.04)}
.review-top{display:flex;align-items:center;gap:10px}
.avatar{width:28px;height:28px;border-radius:50%;background:linear-gradient(135deg,#c9b8a6,#7a6654);flex:none}
.review-top b{font-size:10px;display:block}
.review-top span{font-size:8.5px;color:var(--muted)}
.review-top .stars{margin-left:auto;color:var(--gold);font-size:10px;letter-spacing:1px}
.review p{font-size:9px;color:var(--muted);line-height:1.6;margin-top:10px}
.review-cta{text-align:center;margin-top:30px;font-size:10.5px;color:var(--muted)}
.review-cta .btn{display:flex;width:118px;height:30px;background:var(--teal);font-size:10px;margin:12px auto 0}

/* contact */
.contact{height:614px;background:var(--bg-soft);padding-top:58px}
.contact-grid{display:flex;justify-content:space-between;margin-top:52px}
.contact-left{width:467px}
.mini-row{display:flex;gap:19px}
.mini{width:224px;height:121px;padding:18px 16px}
.mini-icon{width:28px;height:28px;border-radius:6px;display:flex;align-items:center;justify-content:center}
.mini b{font-size:10px;display:block;margin-top:18px}
.mini .hl{font-size:10px;color:var(--teal);display:block;margin-top:4px}
.mini .hl.alt{color:var(--orange)}
.mini small{font-size:8.5px;color:var(--muted);display:block;margin-top:4px}
.visit{height:234px;margin-top:23px;overflow:hidden}
.visit-head{padding:18px 16px;height:92px}
.visit-head b{font-size:11px;display:block}
.visit-head span{font-size:9.5px;color:var(--muted);display:block;margin-top:8px}
.map{height:142px;background:linear-gradient(180deg,#e9ebee,#dde1e5)}
.contact-form{width:469px;height:394px;padding:20px 22px}
.seg{display:flex;background:#eef0f2;border-radius:4px;height:28px;padding:3px}
.seg span{flex:1;display:flex;align-items:center;justify-content:center;font-size:9.5px;color:var(--ink)}
.seg span.on{background:var(--white);color:var(--teal);border-radius:3px}
.contact-form .fields{gap:14px 16px;margin-top:18px}
.contact-form .textarea{height:78px}
.contact-form .submit{height:30px;margin-top:10px}

/* footer */
.footer{height:233px;background:var(--navy);color:#c8ced6;padding-top:32px}
.foot-grid{display:grid;grid-template-columns:246px 246px 246px 228px}
.foot-brand{color:var(--white);font-weight:700;font-size:16px;letter-spacing:.5px}
.foot-grid p{font-size:9px;line-height:1.55;margin-top:10px;width:200px}
.foot-grid h4{font-family:"Inter",sans-serif;color:var(--white);font-size:11px;font-weight:600}
.foot-list{list-style:none;margin-top:12px;font-size:9.5px;line-height:2.1}
.ci{display:flex;gap:8px;font-size:9.5px;margin-top:10px;line-height:1.4}
.hr-list{margin-top:12px}
.hr{display:flex;justify-content:space-between;font-size:9px;line-height:1.9}
.hr b{color:var(--white);font-weight:500}
.foot-bottom{display:flex;justify-content:space-between;align-items:center;margin-top:50px}
.socials{display:flex;gap:14px}
.socials span{width:22px;height:22px;border-radius:50%;background:var(--navy-2);display:block}
.foot-bottom small{font-size:9px}
</style>
</head>
<body>

<header class="nav">
  <div class="brand"><span class="mark"></span>NORTHGATE</div>
  <nav class="nav-links"><span>Home</span><span>Services</span><span>About</span><span>Reviews</span><span>Contact</span></nav>
  <div class="nav-cta">
    <a class="btn bg-teal" href="#request">Request Service</a>
    <a class="btn bg-orange" href="tel:5550142290">
      <svg width="10" height="10" viewBox="0 0 24 24" fill="#fff"><path d="M6.6 10.8a15.1 15.1 0 0 0 6.6 6.6l2.2-2.2a1 1 0 0 1 1-.25 11.4 11.4 0 0 0 3.6.57 1 1 0 0 1 1 1V20a1 1 0 0 1-1 1A17 17 0 0 1 3 4a1 1 0 0 1 1-1h3.5a1 1 0 0 1 1 1c0 1.25.2 2.45.57 3.57a1 1 0 0 1-.25 1z"/></svg>Call Now</a>
  </div>
</header>

<section class="hero">
  <div class="hero-photo" role="img" aria-label="Busy commercial kitchen with stainless steel cooking line under warm light"></div>
  <div class="hero-shade"></div>
  <div class="hero-copy">
    <h1>Kitchen Repair Done Right</h1>
    <p>Fast, reliable service for commercial cooking equipment</p>
    <div class="hero-actions">
      <a class="btn btn-primary" href="#request">Request Service</a>
      <a class="btn btn-ghost" href="#services">Our Services</a>
    </div>
  </div>
  <div class="dots"><span></span><span></span><span></span></div>
</section>

<section class="services" id="services">
  <div class="wrap">
    <div class="section-head">
      <h2>Our Service Highlights</h2>
      <p>Expert repair and maintenance that keeps your kitchen running through every busy service</p>
    </div>
    <div class="tabs">
      <span class="tab active">Cooking Lines</span>
      <span class="tab">Ovens</span>
      <span class="tab">Fryers</span>
      <span class="tab">Dishwashers</span>
    </div>
    <div class="service-grid">
      <article class="service">
        <div class="service-photo" role="img" aria-label="Commercial gas range with open burners" style="background:linear-gradient(135deg,#5a4030,#c8a070 50%,#efe4d6)"><span class="tag">24/7</span></div>
        <div class="service-body"><h3>Range &amp; Griddle Repair</h3><p>Burner, igniter and thermostat repair for gas and electric lines</p><a class="btn" href="#request">Book Service</a></div>
      </article>
      <article class="service">
        <div class="service-photo" role="img" aria-label="Stainless steel convection oven" style="background:linear-gradient(135deg,#eeeae4,#d8a060 55%,#f3efe9)"><span class="tag">Same Day</span></div>
        <div class="service-body"><h3>Oven Service</h3><p>Convection, combi and deck oven diagnostics and calibration</p><a class="btn" href="#request">Book Service</a></div>
      </article>
      <article class="service">
        <div class="service-photo" role="img" aria-label="Commercial deep fryer station" style="background:linear-gradient(135deg,#1e2a22,#4d7a3a 45%,#c03a25 75%,#2b2b2b)"><span class="tag">Certified</span></div>
        <div class="service-body"><h3>Fryer Maintenance</h3><p>Heating element, pilot and safety valve repair with genuine parts</p><a class="btn" href="#request">Book Service</a></div>
      </article>
    </div>
    <div class="services-more"><a class="btn" href="#request">View All Services &amp; Book Online</a></div>
  </div>
</section>

<section class="about">
  <div class="wrap">
    <div class="about-text">
      <h2>About Northgate Service</h2>
      <p>For over a decade, Northgate Restaurant Service has kept commercial kitchens in Maplewood running. We know that when equipment stops, your whole service stops with it.</p>
      <p>Our factory-trained technicians combine deep technical knowledge with quick response times and honest pricing. From a single fryer to a full cooking line, we get you back to business fast.</p>
      <div class="features">
        <div class="feature"><span class="f-icon"><svg width="12" height="12" viewBox="0 0 24 24" fill="none" stroke="#0f8b7e" stroke-width="2"><path d="M5 12l4 4 10-10"/></svg></span><div><h4>Certified Technicians</h4><p>Factory-trained experts on every major equipment brand</p></div></div>
        <div class="feature"><span class="f-icon"><svg width="12" height="12" viewBox="0 0 24 24" fill="none" stroke="#0f8b7e" stroke-width="2"><circle cx="12" cy="12" r="8"/><path d="M12 8v4l3 2"/></svg></span><div><h4>Fast Response</h4><p>Same-day visits and around-the-clock emergency repair</p></div></div>
        <div class="feature"><span class="f-icon"><svg width="12" height="12" viewBox="0 0 24 24" fill="none" stroke="#0f8b7e" stroke-width="2"><rect x="4" y="7" width="16" height="12" rx="2"/><path d="M9 7V5h6v2"/></svg></span><div><h4>Genuine Parts</h4><p>Fully stocked vans with original manufacturer parts</p></div></div>
        <div class="feature"><span class="f-icon"><svg width="12" height="12" viewBox="0 0 24 24" fill="none" stroke="#0f8b7e" stroke-width="2"><path d="M12 3l7 3v6c0 4-3 7-7 9-4-2-7-5-7-9V6z"/></svg></span><div><h4>Preventive Plans</h4><p>Scheduled maintenance that prevents costly breakdowns</p></div></div>
      </div>
    </div>
    <div class="about-visual">
      <div class="tech-photo" role="img" aria-label="Technician servicing equipment in a commercial kitchen"></div>
      <div class="badge-rating"><b>5★</b><span>Customer Rating</span></div>
      <div class="badge-years"><b>10+</b><span>Years of Experience</span></div>
    </div>
  </div>
</section>

<section class="request" id="request">
  <div class="wrap">
    <div class="section-head">
      <h2>Request a Service</h2>
      <p>Tell us what's wrong and when works for you. A technician will confirm your visit quickly.</p>
    </div>
    <div class="request-grid">
      <form class="card req-form">
        <h3>Service Request</h3>
        <div class="fields">
          <div class="field"><label>Full Name *</label><div class="input">Enter your full name</div></div>
          <div class="field"><label>Email Address *</label><div class="input">Enter your email</div></div>
          <div class="field"><label>Phone Number *</label><div class="input">(555) 014-2290</div></div>
          <div class="field"><label>Equipment Type *</label><div class="input sel">Select equipment<span>⌄</span></div></div>
          <div class="field"><label>Preferred Date *</label><div class="input val">dd / mm / yyyy<span>▭</span></div></div>
          <div class="field"><label>Urgency *</label><div class="input sel">Select urgency<span>⌄</span></div></div>
          <div class="field full"><label>Describe the Issue</label><div class="input textarea">Equipment make and model, symptoms, error codes...</div><div class="count">0/500 characters</div></div>
        </div>
        <div class="submit">Submit Request</div>
      </form>
      <div class="req-side">
        <div class="assist">
          <h3>Need Emergency Repair?</h3>
          <a class="assist-item" href="tel:5550142290"><span class="assist-icon"><svg width="12" height="12" viewBox="0 0 24 24" fill="#fff"><path d="M6.6 10.8a15.1 15.1 0 0 0 6.6 6.6l2.2-2.2a1 1 0 0 1 1-.25 11.4 11.4 0 0 0 3.6.57 1 1 0 0 1 1 1V20a1 1 0 0 1-1 1A17 17 0 0 1 3 4a1 1 0 0 1 1-1h3.5a1 1 0 0 1 1 1c0 1.25.2 2.45.57 3.57a1 1 0 0 1-.25 1z"/></svg></span><div><b>Call Us Now</b><span>(555) 014-2290</span></div></a>
          <a class="assist-item" href="sms:5550142290"><span class="assist-icon"><svg width="12" height="12" viewBox="0 0 24 24" fill="none" stroke="#fff" stroke-width="2"><path d="M4 5h16v11H9l-5 4z"/></svg></span><div><b>Text Us</b><span>Send a text to our dispatch team</span></div></a>
        </div>
        <div class="card hours">
          <h3>Service Hours</h3>
          <div class="hours-list">
            <div class="hours-row"><span>Monday - Friday</span><b>7:00 AM - 7:00 PM</b></div>
            <div class="hours-row"><span>Saturday</span><b>8:00 AM - 4:00 PM</b></div>
            <div class="hours-row"><span>Emergency Repair</span><b>24 Hours, 7 Days</b></div>
          </div>
        </div>
      </div>
    </div>
  </div>
</section>

<section class="reviews">
  <div class="wrap">
    <div class="section-head">
      <h2>What Our Clients Say</h2>
      <p>Don't just take our word for it. Here's what restaurant owners and kitchen managers say about our service.</p>
    </div>
    <div class="review-grid">
      <div class="review"><div class="review-top"><span class="avatar" role="img" aria-label="Client portrait"></span><div><b>Nora Whitfield</b><span>2 weeks ago</span></div><span class="stars">★★★★★</span></div><p>"Our fryer went down on a Friday night and they had a tech here within two hours. Fixed on the spot with the right part. Saved our whole weekend."</p></div>
      <div class="review"><div class="review-top"><span class="avatar" role="img" aria-label="Client portrait"></span><div><b>Daniel Ortega</b><span>1 month ago</span></div><span class="stars">★★★★★</span></div><p>"The best equipment service in Maplewood! Their technician explained the problem clearly and the combi oven runs better than ever. Highly recommend!"</p></div>
      <div class="review"><div class="review-top"><span class="avatar" role="img" aria-label="Client portrait"></span><div><b>Priya Lawson</b><span>3 weeks ago</span></div><span class="stars">★★★★★</span></div><p>"We signed up for their maintenance plan and haven't had a breakdown since. Punctual, tidy and honest about what really needs replacing."</p></div>
      <div class="review"><div class="review-top"><span class="avatar" role="img" aria-label="Client portrait"></span><div><b>Marcus Bell</b><span>1 week ago</span></div><span class="stars">★★★★★</span></div><p>"Outstanding work on our range and griddle. Clear pricing, genuine parts and a technician who clearly knows commercial kitchens inside out."</p></div>
      <div class="review"><div class="review-top"><span class="avatar" role="img" aria-label="Client portrait"></span><div><b>Hannah Greer</b><span>2 months ago</span></div><span class="stars">★★★★★</span></div><p>"They service all three of our locations. Booking by text is easy and the team always shows up when promised. Will definitely keep using them!"</p></div>
    </div>
    <div class="review-cta">Happy with our service? We'd love to hear from you!<a class="btn" href="#">Leave a Review</a></div>
  </div>
</section>

<section class="contact">
  <div class="wrap">
    <div class="section-head">
      <h2>Get In Touch</h2>
      <p>Have questions about repairs or maintenance plans? We're here to help. Contact us for any inquiry.</p>
    </div>
    <div class="contact-grid">
      <div class="contact-left">
        <div class="mini-row">
          <div class="card mini"><span class="mini-icon" style="background:var(--teal-soft)"><svg width="12" height="12" viewBox="0 0 24 24" fill="#0f8b7e"><path d="M6.6 10.8a15.1 15.1 0 0 0 6.6 6.6l2.2-2.2a1 1 0 0 1 1-.25 11.4 11.4 0 0 0 3.6.57 1 1 0 0 1 1 1V20a1 1 0 0 1-1 1A17 17 0 0 1 3 4a1 1 0 0 1 1-1h3.5a1 1 0 0 1 1 1c0 1.25.2 2.45.57 3.57a1 1 0 0 1-.25 1z"/></svg></span><b>Call Us</b><a class="hl" href="tel:5550142290">(555) 014-2290</a><small>24/7 emergency repair line</small></div>
          <div class="card mini"><span class="mini-icon" style="background:var(--orange-soft)"><svg width="12" height="12" viewBox="0 0 24 24" fill="none" stroke="#f47a1c" stroke-width="2"><rect x="3" y="5" width="18" height="14" rx="2"/><path d="M3 7l9 6 9-6"/></svg></span><b>Email Us</b><span class="hl alt">info@northgateservice.com</span><small>We'll respond within 24 hours</small></div>
        </div>
        <div class="card visit">
          <div class="visit-head"><b>Visit Our Service Center</b><span>48 Harbor Lane, Old Town District, Maplewood, IL 62704</span></div>
          <div class="map" role="img" aria-label="Street map showing the service center location"></div>
        </div>
      </div>
      <form class="card contact-form">
        <div class="seg"><span class="on">General Contact</span><span>Maintenance Plans</span></div>
        <div class="fields">
          <div class="field"><label>Full Name *</label><div class="input">Enter your name</div></div>
          <div class="field"><label>Email Address *</label><div class="input">Enter your email</div></div>
          <div class="field"><label>Phone Number</label><div class="input">(555) 014-2290</div></div>
          <div class="field"><label>Subject *</label><div class="input sel">Select subject<span>⌄</span></div></div>
          <div class="field full"><label>Message *</label><div class="input textarea">Tell us how we can help you...</div><div class="count">0/500 characters</div></div>
        </div>
        <div class="submit">Send Message</div>
      </form>
    </div>
  </div>
</section>

<footer class="footer">
  <div class="wrap">
    <div class="foot-grid">
      <div><div class="foot-brand">NORTHGATE</div><p>Expert repair and maintenance for commercial cooking equipment, keeping kitchens running safely and on time.</p></div>
      <div><h4>Quick Links</h4><ul class="foot-list"><li>Home</li><li>Services</li><li>About Us</li><li>Service Request</li></ul></div>
      <div><h4>Contact Info</h4>
        <div class="ci"><svg width="10" height="10" viewBox="0 0 24 24" fill="#0f8b7e"><path d="M12 2a7 7 0 0 0-7 7c0 5 7 13 7 13s7-8 7-13a7 7 0 0 0-7-7zm0 9.5A2.5 2.5 0 1 1 12 6.5a2.5 2.5 0 0 1 0 5z"/></svg><span>48 Harbor Lane, Old Town District, Maplewood, IL 62704</span></div>
        <div class="ci"><svg width="10" height="10" viewBox="0 0 24 24" fill="#0f8b7e"><path d="M6.6 10.8a15.1 15.1 0 0 0 6.6 6.6l2.2-2.2a1 1 0 0 1 1-.25 11.4 11.4 0 0 0 3.6.57 1 1 0 0 1 1 1V20a1 1 0 0 1-1 1A17 17 0 0 1 3 4a1 1 0 0 1 1-1h3.5a1 1 0 0 1 1 1c0 1.25.2 2.45.57 3.57a1 1 0 0 1-.25 1z"/></svg><span>(555) 014-2290</span></div>
        <div class="ci"><svg width="10" height="10" viewBox="0 0 24 24" fill="none" stroke="#0f8b7e" stroke-width="2"><rect x="3" y="5" width="18" height="14" rx="2"/><path d="M3 7l9 6 9-6"/></svg><span>info@northgateservice.com</span></div>
      </div>
      <div><h4>Hours</h4><div class="hr-list">
        <div class="hr"><span>Monday - Friday</span><b>7:00 AM - 7:00 PM</b></div>
        <div class="hr"><span>Saturday</span><b>8:00 AM - 4:00 PM</b></div>
        <div class="hr"><span>Emergency</span><b>24 Hours, 7 Days</b></div>
      </div></div>
    </div>
    <div class="foot-bottom">
      <div class="socials"><span></span><span></span><span></span><span></span></div>
      <small>© 2024 Northgate Restaurant Service. All rights reserved.</small>
    </div>
  </div>
</footer>

</body>
</html>
```